Building Company Business Card Design

I am looking to get a business card designed for my Building Company. Please find the logo attached.

Industry/Entity Type

Business

Contact Information for Business Card

Mobile 0472 913 706
Email admin@harbourlineconstruct.com.au
Website www.harbourlineconstruct.com.au

Colors
0255a3

```html
<!DOCTYPE html>
<html lang="en">
<head>
<meta charset="utf-8">
<title>Harbourline Construct – Business Card</title>
<link href="https://fonts.googleapis.com/css2?family=Montserrat:wght@500;600;700&family=Lato:wght@400&display=swap" rel="stylesheet">
<style>
  :root {
    --stage: #202020;
    --brand-blue: #0f56a4;
    --accent-blue: #0255a3;
    --slate: #6d6e71;
    --ink: #222222;
    --paper: #ffffff;
  }
  * { margin: 0; padding: 0; box-sizing: border-box; }
  html, body { width: 1200px; height: 900px; overflow: hidden; }
  body { background: var(--stage); position: relative; font-family: "Lato", sans-serif; }

  .card { position: absolute; top: 306px; width: 440px; height: 271px; overflow: hidden; }
  .card-front { left: 149px; background: var(--paper); }
  .card-back { left: 608px; width: 441px; background: var(--brand-blue); }

  .corner-marks { position: absolute; left: 0; top: 26px; }

  .holder { position: absolute; left: 39px; top: 29px; }
  .holder-name { font-family: "Montserrat", sans-serif; font-size: 16px; font-weight: 600; letter-spacing: 0.2px; color: var(--slate); line-height: 1; }
  .holder-name .first { color: var(--accent-blue); }
  .holder-role { font-size: 11.5px; color: var(--ink); margin-top: 4px; }

  .wordmark { position: absolute; font-family: "Montserrat", sans-serif; font-weight: 700; letter-spacing: 0.5px; line-height: 1; display: flex; align-items: center; gap: 8px; }
  .wordmark-front { right: 18px; top: 106px; font-size: 22px; color: var(--accent-blue); }
  .wordmark-back { left: 0; right: 0; top: 123px; justify-content: center; font-size: 24px; color: var(--paper); }
  .wordmark .dot { width: 10px; height: 10px; background: currentColor; }

  .contacts { position: absolute; left: 23px; top: 186px; list-style: none; }
  .contacts li { display: flex; align-items: center; gap: 5px; font-size: 12.5px; color: var(--ink); height: 16px; }
  .contacts svg { width: 10px; height: 10px; fill: var(--accent-blue); }

  .footer-band { position: absolute; left: 0; bottom: 0; }
</style>
</head>
<body>
  <section class="card card-front" aria-label="Business card front">
    <svg class="corner-marks" width="30" height="37" viewBox="0 0 30 37">
      <polygon points="0,0 12,0 16,37 0,37" fill="var(--slate)"/>
      <polygon points="12,0 29,0 29,37 16,37" fill="var(--accent-blue)"/>
    </svg>

    <div class="holder">
      <p class="holder-name"><span class="first">DANIEL</span> CARVER</p>
      <p class="holder-role">Managing Director</p>
    </div>

    <div class="wordmark wordmark-front"><span class="dot"></span>HARBOURLINE CONSTRUCT</div>

    <ul class="contacts">
      <li><svg viewBox="0 0 10 10"><path d="M2 0.5l1.6 2-1 1.1c.6 1.3 1.6 2.3 2.9 2.9l1.1-1 2 1.6-1 1.9C4.6 8.8 1.2 5.4.1 1.5z"/></svg>0472 913 706</li>
      <li><svg viewBox="0 0 10 10"><path d="M0 2h10v6H0z M0 2l5 3.5L10 2" stroke="#fff" stroke-width="0.8"/></svg>admin@harbourlineconstruct.com.au</li>
      <li><svg viewBox="0 0 10 10"><circle cx="5" cy="5" r="4.6"/><path d="M1 5h8M5 .5v9" stroke="#fff" stroke-width="0.6" fill="none"/></svg>www.harbourlineconstruct.com.au</li>
    </ul>

    <svg class="footer-band" width="440" height="21" viewBox="0 0 440 21">
      <polygon points="0,6 238,6 225,21 0,21" fill="var(--slate)"/>
      <polygon points="243,0 440,0 440,21 227,21" fill="var(--accent-blue)"/>
    </svg>
  </section>

  <section class="card card-back" aria-label="Business card back">
    <div class="wordmark wordmark-back"><span class="dot"></span>HARBOURLINE CONSTRUCT</div>
  </section>
</body>
</html>
```